Stanbrook Fire Services Pty Ltd

We need business cards for a company based in Perth, we install, service and maintain fire equipment.
On the front we want a great design with our logo and a small spot for our full company name, general company email address and office number. On the back we need space for our name, title, mobile number and email address on the back.

Target Market(s)

Facility managers and commercial/industrial building owners/occupiers.

Contact Information for Business Card

Font styles to use
Sans Serif

Requirements
Must have
• Please only submit 5 of your best samples.
Darker tones are preferred.
Nice to have
• We want to use, black, red and grey. Keep it modern and clean.
I've attached the company logo and a sample of a boarder we use on our emergency plans.
Should not have
• No preference. Let the designer choose.

```html
<!DOCTYPE html>
<html lang="en">
<head>
<meta charset="utf-8">
<title>Stanbrook Fire Services – Business Card</title>
<link rel="stylesheet" href="https://fonts.googleapis.com/css2?family=Roboto:wght@400;500;700;900&display=swap">
<style>
  :root {
    --backdrop: #2b2b2c;
    --card-white: #ffffff;
    --card-black: #1c1d1f;
    --brand-red: #e41e26;
    --text-grey: #555555;
    --rule-grey: #8a8a8a;
  }
  * { box-sizing: border-box; margin: 0; padding: 0; }
  html, body {
    width: 1200px;
    height: 1108px;
    overflow: hidden;
    background: var(--backdrop);
    font-family: "Roboto", Arial, sans-serif;
  }
  .stage {
    position: relative;
    width: 1200px;
    height: 1108px;
  }
  .card {
    position: absolute;
    top: 204px;
    width: 400px;
    height: 700px;
    border-radius: 26px;
    overflow: hidden;
  }
  .card--front { left: 150px; background: var(--card-white); }
  .card--back  { left: 650px; background: var(--card-black); }

  .brand {
    position: absolute;
    left: 0;
    right: 0;
    display: flex;
    align-items: center;
    justify-content: center;
    gap: 14px;
    color: var(--brand-red);
    font-weight: 900;
    font-size: 46px;
    letter-spacing: 1px;
  }
  .brand__square {
    width: 26px;
    height: 26px;
    background: var(--brand-red);
  }
  .card--front .brand { top: 110px; }
  .card--back  .brand { top: 320px; }

  .contact {
    position: absolute;
    left: 0;
    right: 0;
    top: 362px;
    text-align: center;
    color: var(--text-grey);
  }
  .contact__name {
    color: var(--brand-red);
    font-weight: 700;
    font-size: 26px;
  }
  .contact__title {
    font-size: 20px;
    margin-top: 2px;
  }
  .contact__divider {
    position: relative;
    width: 230px;
    height: 30px;
    margin: 6px auto 4px;
    display: flex;
    align-items: center;
    justify-content: center;
    gap: 5px;
  }
  .contact__divider::before {
    content: "";
    position: absolute;
    left: 0; right: 0; top: 50%;
    height: 1.5px;
    background: var(--rule-grey);
    z-index: 0;
  }
  .icon {
    position: relative;
    z-index: 1;
    width: 24px;
    height: 24px;
  }
  .contact__lines {
    font-size: 20px;
    line-height: 30px;
  }
  .contact__web { color: var(--brand-red); }
  .contact__rule {
    width: 230px;
    height: 1.5px;
    background: var(--rule-grey);
    margin: 12px auto 14px;
  }
  .contact__address {
    font-size: 20px;
    line-height: 26px;
  }
</style>
</head>
<body>
<main class="stage">
  <section class="card card--front">
    <div class="brand">
      <span class="brand__square"></span>
      <span class="brand__name">STANBROOK</span>
    </div>

    <div class="contact">
      <p class="contact__name">Daniel Hart</p>
      <p class="contact__title">Manager</p>
      <div class="contact__divider">
        <svg class="icon" viewBox="0 0 24 24" aria-label="Phone">
          <circle cx="12" cy="12" r="12" fill="var(--brand-red)"/>
          <path d="M8 7c1-1 2 0 2.5 1.2l.5 1.3c.2.5-.2 1-.6 1.3.6 1.3 1.5 2.2 2.8 2.8.3-.4.8-.8 1.3-.6l1.3.5c1.2.5 2.2 1.5 1.2 2.5-1 1-3 1.2-5.5-.8-2.5-2-4.5-4.7-3.9-6.9.1-.6.2-1 .4-1.3z" fill="#fff"/>
        </svg>
        <svg class="icon" viewBox="0 0 24 24" aria-label="Email">
          <circle cx="12" cy="12" r="12" fill="var(--brand-red)"/>
          <rect x="6" y="8" width="12" height="8" fill="none" stroke="#fff" stroke-width="1.6"/>
          <path d="M6 8l6 5 6-5" fill="none" stroke="#fff" stroke-width="1.6"/>
        </svg>
        <svg class="icon" viewBox="0 0 24 24" aria-label="Website">
          <circle cx="12" cy="12" r="12" fill="var(--brand-red)"/>
          <circle cx="12" cy="12" r="6" fill="none" stroke="#fff" stroke-width="1.5"/>
          <ellipse cx="12" cy="12" rx="2.5" ry="6" fill="none" stroke="#fff" stroke-width="1.3"/>
          <path d="M6 12h12" stroke="#fff" stroke-width="1.3"/>
        </svg>
      </div>
      <div class="contact__lines">
        <p>123-456-2100</p>
        <p>office@stanbrookfire.com</p>
        <p>www.<span class="contact__web">yourwebsite</span>.com</p>
      </div>
      <div class="contact__rule"></div>
      <div class="contact__address">
        <p>Your address, city</p>
        <p>state, ZIP 0000</p>
      </div>
    </div>
  </section>

  <section class="card card--back">
    <div class="brand">
      <span class="brand__square"></span>
      <span class="brand__name">STANBROOK</span>
    </div>
  </section>
</main>
</body>
</html>
```